Kestrel.Construction Truck Wrap

We are a whole house construction company for residential as well as commercial. We need a truck wrap for a our 2017 vdx 4800 crew cab.
We specialize in really everything but the biggest things is exterior (roofing/gutters/siding). Our colors are white,grey, black, and neon baby blue. our font for our logo is earth orbiter you can download from here (https://www.glyphbarn.net/earth-orbiter.font) You can change the logo were open to ideas. please dont add a circle with an arrow going around or something like that, were not into that.
We like a something that is very eye popping, maybe slight crazy.
Something that when we are driving people will have to look. In the files you will find images of designs that we like but you do not have to copy or anything like that, they are there just to represent the direction. as well as Files that have our logo and some of our current marketing materials. We are going to be changing those soon as well.
Construction
- Earth Orbiter
- Also please incorporate the rear drivers and passengers side window as well as the rear window. please refer more to all the images i posted and see the crazyiness going on in those.
- must attract attention at first glance

```html
<!DOCTYPE html>
<html lang="en">
<head>
<meta charset="utf-8">
<title>Kestrel Construction Truck Wrap</title>
<link rel="stylesheet" href="https://fonts.googleapis.com/css2?family=Audiowide&display=swap">
<style>
  :root {
    --stage: #4d4d4d;
    --wrap-black: #050607;
    --wrap-white: #ffffff;
    --neon-blue: #2ea3da;
    --deep-navy: #0d2233;
    --logo-grey: #d8dde2;
    --cut-line: #d8282a;
    --ink: #0b0b0b;
  }
  html, body {
    margin: 0;
    padding: 0;
    width: 1200px;
    height: 1176px;
    overflow: hidden;
    background: var(--stage);
  }
  .wrap-sheet {
    display: block;
    width: 1200px;
    height: 1176px;
  }
  .body-dark { fill: var(--wrap-black); }
  .body-light { fill: var(--wrap-white); }
  .accent-band { fill: var(--neon-blue); }
  .glass-cutout { fill: var(--stage); }
  .cut-line { fill: none; stroke: var(--cut-line); stroke-width: 1.4; }
  .brand-name {
    font-family: "Audiowide", sans-serif;
    font-size: 15px;
    letter-spacing: 0.4px;
  }
  .brand-tagline {
    font-family: "Audiowide", sans-serif;
    font-size: 7.5px;
    letter-spacing: 0.6px;
    fill: var(--neon-blue);
  }
  .service-line {
    font-family: "Audiowide", sans-serif;
    font-size: 17px;
  }
  .service-headline {
    font-family: "Audiowide", sans-serif;
    font-size: 32px;
    fill: var(--deep-navy);
  }
  .phone-number {
    font-family: "Audiowide", sans-serif;
    font-size: 40px;
  }
  .on-dark .brand-name { fill: var(--logo-grey); }
  .on-dark .service-line,
  .on-dark .phone-number { fill: var(--wrap-white); }
  .on-light .brand-name,
  .on-light .service-line,
  .on-light .phone-number { fill: var(--ink); }
</style>
</head>
<body>
<svg class="wrap-sheet" viewBox="60 380 1380 1177" xmlns="http://www.w3.org/2000/svg">
  <defs>
    <path id="truck-body" d="M92,768 L95,755 C200,745 300,738 330,735 L378,742 C420,718 470,688 520,660 L525,640 L565,625 L860,610 L885,612 C897,616 901,640 905,700 L910,725 L1390,712 L1405,715 L1407,735 L1390,740 L1390,800 L1355,800 L1355,825 L1407,828 L1407,855 L1378,860 L1360,860 L1310,928 L1285,930 L1275,810 C1270,790 1240,775 1200,778 L1090,785 C1065,790 1055,810 1055,830 L1040,905 L390,962 L360,840 C350,815 320,805 290,808 L200,812 C170,815 160,840 160,860 L95,868 L95,842 L135,842 L138,790 L92,790 Z"/>
    <path id="accent-sweep" d="M903,610 C910,700 885,770 800,808 C700,852 510,872 455,930 C440,945 432,958 425,970 L470,975 C520,940 600,915 720,890 C850,862 960,830 1060,800 L1410,705 L1410,690 L903,690 Z"/>
    <path id="front-glass" d="M450,722 C480,690 530,652 560,642 L640,637 C645,637 648,640 648,645 L648,742 L485,745 L478,752 Z"/>
    <path id="rear-glass" d="M688,640 L860,633 C866,633 868,636 868,640 L866,735 C866,740 862,742 856,742 L690,745 Z"/>
    <clipPath id="body-clip"><use href="#truck-body"/></clipPath>
    <g id="cut-lines">
      <use href="#truck-body" class="cut-line"/>
      <path class="cut-line" d="M402,745 L405,940 L430,942"/>
      <path class="cut-line" d="M665,630 L668,948"/>
      <path class="cut-line" d="M895,640 L898,925 L668,945"/>
      <path class="cut-line" d="M165,862 C175,835 200,825 260,822 L300,820 C335,820 350,840 360,870"/>
      <path class="cut-line" d="M1065,840 C1070,810 1090,798 1120,796 L1200,792 C1240,790 1262,805 1268,830 L1278,925"/>
      <rect class="cut-line" x="590" y="774" width="64" height="11" rx="5"/>
      <rect class="cut-line" x="825" y="767" width="64" height="11" rx="5"/>
    </g>
  </defs>

  <g class="template on-dark" role="img" aria-label="Black truck wrap with neon blue sweep and faint blueprint line drawing texture">
    <use href="#truck-body" class="body-dark"/>
    <g clip-path="url(#body-clip)">
      <use href="#accent-sweep" class="accent-band"/>
    </g>
    <use href="#front-glass" class="glass-cutout"/>
    <use href="#rear-glass" class="glass-cutout"/>
    <use href="#cut-lines"/>
    <text class="brand-name" x="415" y="806">KESTREL CONSTRUCTION</text>
    <text class="brand-tagline" x="417" y="819">HOMES, ROOFS AND SIDING DONE RIGHT</text>
    <text class="service-line" x="570" y="862" transform="rotate(-15 570 862)">INTERIOR-EXTERIOR</text>
    <text class="service-headline" x="522" y="912" transform="rotate(-15 522 912)">BUILD AND DESIGN</text>
    <text class="phone-number" x="720" y="916" transform="rotate(-15 720 916)">555-014-2290</text>
  </g>

  <g class="template on-light" transform="translate(0 430)" role="img" aria-label="White truck wrap with neon blue sweep and faint blueprint line drawing texture">
    <use href="#truck-body" class="body-light"/>
    <g clip-path="url(#body-clip)">
      <use href="#accent-sweep" class="accent-band"/>
    </g>
    <use href="#front-glass" class="glass-cutout"/>
    <use href="#rear-glass" class="glass-cutout"/>
    <use href="#cut-lines"/>
    <text class="brand-name" x="415" y="806">KESTREL CONSTRUCTION</text>
    <text class="brand-tagline" x="417" y="819">HOMES, ROOFS AND SIDING DONE RIGHT</text>
    <text class="service-line" x="570" y="862" transform="rotate(-15 570 862)">INTERIOR-EXTERIOR</text>
    <text class="service-headline" x="522" y="912" transform="rotate(-15 522 912)">BUILD AND DESIGN</text>
    <text class="phone-number" x="720" y="916" transform="rotate(-15 720 916)">555-014-2290</text>
  </g>
</svg>
</body>
</html>
```